Design and Renovation Company Luxury Business Card

I want to create a luxury business card for a Design and Renovation Firm . We will use our current logo. The company name is 742BUILD. We do not want anything standard. We need a very unique concept.
Please see uploaded inspiration. I really like the textured paper option. I would like the card to be thick with debossing, and/or embossing options. The logo has orange in it but I would like to see the card with and without the orange. I think the orange may make the company feel less high-end. The goal is to elevate the logo not match its vibe per se of the logo. We want something very unique, not standard at all!
I would like a space for :
Logo,
Name,
Position,
Email,
Office number,
Website Address,
Business Address,
Thank you!
Have fun!
Target Market(s)
Home owners Age 35 +
Industry/Entity Type
Design and Renovation
Contact Information for Business Card
Logo, Name, Position, Email, Office number, Website Address, Business Address,.
Colors
Designer to choose colors to be used in the design.
Requirements
Must have
- A luxury designer feel. Must be black or dark grey but open to other luxury ideas.
Nice to have
- Gold, silver, black embossing or debossing. Textured paper design.
Should not have
- A cheap look and feel.

```html
<!DOCTYPE html>
<html lang="en">
<head>
<meta charset="utf-8">
<title>742BUILD Business Card</title>
<link rel="stylesheet" href="https://fonts.googleapis.com/css2?family=Saira:wght@400;500;700&display=swap">
<style>
  :root {
    --backdrop: #2a2a2b;
    --card: #1f1f20;
    --card-edge: #181819;
    --orange: #f7931e;
    --silver: #b9b9b9;
    --text-light: #d8d8d8;
    --deboss: #111112;
  }
  * { box-sizing: border-box; margin: 0; padding: 0; }
  html, body { width: 1200px; height: 799px; overflow: hidden; }
  body {
    background: var(--backdrop);
    font-family: "Saira", sans-serif;
    position: relative;
  }
  .card {
    position: absolute;
    top: 235px;
    width: 525px;
    height: 300px;
    background: var(--card);
    border: 1px solid var(--card-edge);
    box-shadow: 0 18px 40px rgba(0,0,0,.45);
  }
  .card--front { left: 45px; }
  .card--back { left: 630px; }

  /* Front */
  .brand__name {
    position: absolute;
    left: 0; right: 0; top: 106px;
    text-align: center;
    font-weight: 500;
    font-size: 54px;
    letter-spacing: 4px;
    color: var(--deboss);
    line-height: 1;
    text-shadow: 0 1px 0 rgba(255,255,255,.06);
  }
  .brand__tagline {
    position: absolute;
    left: 0; right: 0; top: 172px;
    text-align: center;
    font-size: 13px;
    letter-spacing: 5px;
    color: var(--deboss);
    text-shadow: 0 1px 0 rgba(255,255,255,.06);
  }

  /* Back */
  .person {
    position: absolute;
    left: 30px; top: 100px;
    width: 196px;
    text-align: right;
  }
  .person__name {
    font-weight: 700;
    font-size: 25px;
    color: var(--orange);
    line-height: 1.1;
    letter-spacing: .5px;
    white-space: nowrap;
  }
  .person__role {
    font-size: 14px;
    color: var(--text-light);
    margin-top: 4px;
  }
  .divider {
    position: absolute;
    left: 246px; top: 88px;
    width: 1.5px; height: 80px;
    background: var(--orange);
  }
  .contacts {
    position: absolute;
    left: 264px; top: 86px;
    list-style: none;
    font-size: 11.5px;
    color: var(--text-light);
    line-height: 1.35;
  }
  .contacts li { display: flex; gap: 8px; margin-bottom: 3px; }
  .contacts svg { width: 11px; height: 11px; flex: none; margin-top: 2px; fill: var(--orange); }
  .mini-brand {
    position: absolute;
    right: 28px; bottom: 24px;
    font-size: 10px;
    letter-spacing: 1.5px;
    color: var(--silver);
  }
</style>
</head>
<body>
  <section class="card card--front">
    <p class="brand__name">742BUILD</p>
    <p class="brand__tagline">Design and Renovation Firm</p>
  </section>

  <section class="card card--back">
    <div class="person">
      <h1 class="person__name">DANIEL REYES</h1>
      <p class="person__role">Founder &amp; CEO</p>
    </div>
    <div class="divider"></div>
    <ul class="contacts">
      <li>
        <svg viewBox="0 0 12 12"><path d="M6 0a4 4 0 0 0-4 4c0 3 4 8 4 8s4-5 4-8a4 4 0 0 0-4-4zm0 5.5A1.5 1.5 0 1 1 6 2.5a1.5 1.5 0 0 1 0 3z"/></svg>
        <span>58 Alder Row, Marlow Bay<br>Kent County, 40219</span>
      </li>
      <li>
        <svg viewBox="0 0 12 12"><path d="M2.5 0.5l2 2.5-1.2 1.4a7 7 0 0 0 4.3 4.3L9 7.5l2.5 2-1.3 2C5 11.5 .5 7 .5 1.8z"/></svg>
        <span>+1 555 014 7736</span>
      </li>
      <li>
        <svg viewBox="0 0 12 12"><path d="M0 2h12v8H0zM1 3l5 3.5L11 3v-.1H1z" fill-rule="evenodd"/></svg>
        <span>hello@742build.example</span>
      </li>
      <li>
        <svg viewBox="0 0 12 12"><circle cx="6" cy="6" r="5.5"/><path d="M3 4h2l1 2-2 1zm4 3h2l-1 2z" fill="#1f1f20"/></svg>
        <span>742build.example</span>
      </li>
    </ul>
    <p class="mini-brand">742BUILD</p>
  </section>
</body>
</html>
```